Business card design Needed for new logo / Construction business, home extensions and new builds

We need a business card design using our new logo files which i will attach to this project :)

We are a small construction business specialising in home extensions, new builds and property development. We are very ambitious and would appreciate professional and elegant designs for our new business card.

Very serious about using the services on Sketchwharf and recently acquired our new logo from here :)

Please get involved, i will feedback when i can as i am very busy but can respond daily, thanks

Target Market(s)

People that want to build onto their houses, new building developments or adding too their existing property

Industry/Entity Type

Construction

Contact Information for Business Card

Thornley Pike Construction, Wilbur Fenwick (Managing Director), Tel 07829456172, email - info@thornley-pike, www.thornley-pike.co.uk

Colors

Designer to choose colors to be used in the design.

Requirements
Must have
• I like a deep grey on the back please. A lot of you have provided black from and back, try mixing things up a little. The black looks cool 😎 Thanks

```html
<!DOCTYPE html>
<html lang="en">
<head>
<meta charset="utf-8">
<title>Thornley Pike Construction – Business Card</title>
<link rel="stylesheet" href="https://fonts.googleapis.com/css2?family=Montserrat:wght@400;600;700&display=swap">
<style>
  :root{
    --stage:#4a4a4d;
    --card-front:#161616;
    --card-back:#2a2a2d;
    --gold:#e2a92a;
    --gold-deep:#c1842a;
    --gold-light:#f6d27e;
    --silver:#c9ccd0;
    --silver-dark:#8e9297;
    --white:#f2f2f2;
  }
  *{margin:0;padding:0;box-sizing:border-box}
  html,body{width:1200px;height:689px;overflow:hidden}
  body{
    background:var(--stage);
    font-family:"Montserrat",sans-serif;
    position:relative;
  }
  .card{
    position:absolute;
    top:196px;
    width:520px;
    height:297px;
    border-radius:16px;
    overflow:hidden;
    box-shadow:0 18px 40px rgba(0,0,0,.45);
  }
  .card--back{left:50px;background:var(--card-back)}
  .card--front{left:630px;background:var(--card-front)}
  .card__art{position:absolute;inset:0;width:100%;height:100%}

  /* brand name */
  .brand{
    position:absolute;
    display:flex;
    align-items:center;
    gap:12px;
    color:var(--silver);
    font-weight:600;
    text-transform:uppercase;
    white-space:nowrap;
  }
  .brand__mark{background:var(--gold);flex:none}
  .brand__text{display:flex;flex-direction:column;line-height:1.15}
  .card--back .brand{left:50%;top:50%;transform:translate(-50%,-50%);gap:14px}
  .card--back .brand__mark{width:32px;height:32px}
  .card--back .brand__name{font-size:30px;letter-spacing:2px}
  .card--back .brand__sub{font-size:15px;letter-spacing:9.4px;color:var(--gold)}
  .card--front .brand{right:30px;top:62px;gap:9px}
  .card--front .brand__mark{width:16px;height:16px}
  .card--front .brand__text{align-items:flex-end}
  .card--front .brand__name{font-size:16px;letter-spacing:1px}
  .card--front .brand__sub{font-size:9.5px;letter-spacing:3.4px;color:var(--gold)}

  /* person */
  .person{position:absolute;left:38px;top:140px;white-space:nowrap}
  .person__name{color:var(--gold);font-weight:700;font-size:22px;letter-spacing:.5px;text-transform:uppercase}
  .person__role{color:var(--white);font-size:13px;margin-top:2px}

  .divider{position:absolute;left:38px;right:30px;top:196px;height:1px;background:var(--gold)}

  .contacts{position:absolute;left:38px;top:208px;list-style:none}
  .contacts li{display:flex;align-items:center;gap:8px;color:var(--white);font-size:12.5px;height:20px;white-space:nowrap}
  .contacts svg{width:11px;height:11px;fill:var(--gold);flex:none}

  .address{position:absolute;right:30px;top:210px;text-align:right;color:var(--white);font-size:12.5px;line-height:20px;font-style:normal;white-space:nowrap}
</style>
</head>
<body>

  <section class="card card--back" aria-label="Card back">
    <div class="brand">
      <span class="brand__mark"></span>
      <span class="brand__text">
        <span class="brand__name">Thornley Pike</span>
        <span class="brand__sub">Construction</span>
      </span>
    </div>
  </section>

  <section class="card card--front" aria-label="Card front">
    <svg class="card__art" viewBox="0 0 520 297" aria-hidden="true">
      <defs>
        <linearGradient id="goldSweep" x1="0" y1="1" x2="1" y2="0">
          <stop offset="0" stop-color="#c1842a"/>
          <stop offset=".45" stop-color="#d9a04a"/>
          <stop offset=".62" stop-color="#f6d27e"/>
          <stop offset="1" stop-color="#e2a92a"/>
        </linearGradient>
        <linearGradient id="goldBand" x1="0" x2="1">
          <stop offset="0" stop-color="#c1842a"/>
          <stop offset=".6" stop-color="#f6d27e"/>
          <stop offset="1" stop-color="#e2a92a"/>
        </linearGradient>
        <linearGradient id="silverBand" x1="0" x2="1">
          <stop offset="0" stop-color="#8e9297"/>
          <stop offset=".5" stop-color="#e6e8ea"/>
          <stop offset="1" stop-color="#a3a7ac"/>
        </linearGradient>
      </defs>
      <path class="sweep-gold" d="M0 0 H520 V14 C430 18 330 40 250 80 C170 118 90 128 0 128 Z" fill="url(#goldSweep)"/>
      <path class="sweep-silver" d="M0 136 C95 136 175 126 255 88 C335 48 430 26 520 22" fill="none" stroke="url(#silverBand)" stroke-width="5"/>
      <rect class="band-gold" x="0" y="282" width="340" height="15" fill="url(#goldBand)"/>
      <rect class="band-silver" x="345" y="282" width="175" height="15" fill="url(#silverBand)"/>
    </svg>

    <div class="brand">
      <span class="brand__mark"></span>
      <span class="brand__text">
        <span class="brand__name">Thornley Pike</span>
        <span class="brand__sub">Construction</span>
      </span>
    </div>

    <div class="person">
      <p class="person__name">Wilbur Fenwick</p>
      <p class="person__role">Managing Director</p>
    </div>

    <div class="divider"></div>

    <ul class="contacts">
      <li>
        <svg viewBox="0 0 24 24"><path d="M6.6 10.8a15.1 15.1 0 0 0 6.6 6.6l2.2-2.2a1 1 0 0 1 1-.25 11.4 11.4 0 0 0 3.6.57 1 1 0 0 1 1 1V20a1 1 0 0 1-1 1A17 17 0 0 1 3 4a1 1 0 0 1 1-1h3.5a1 1 0 0 1 1 1c0 1.25.2 2.45.57 3.6a1 1 0 0 1-.25 1z"/></svg>
        07829456172
      </li>
      <li>
        <svg viewBox="0 0 24 24"><path d="M2 5h20v14H2zM4 7v.5l8 5 8-5V7z"/></svg>
        info@thornley-pike.co.uk
      </li>
      <li>
        <svg viewBox="0 0 24 24"><circle cx="12" cy="12" r="10"/></svg>
        www.thornley-pike.co.uk
      </li>
    </ul>

    <address class="address">Your address, City<br>State, Zip 1234</address>
  </section>

</body>
</html>
```